A taxi bidding business needs Web Design

We need a cutting edge, super UX-intuitive, Elegant web design for our business called Farovo.

Farovo is Australia based Kind of "Next Lyndo" business where user creates a trip and cabs/drivers place bids on fares/bookings/trips and lowest bidder gets the job.
User can also share the Cabs going in same route to get lowest bids.

- The design needs to be very, very intuitive to use and navigate. Please do not use much of yellow color.

References: StayMoor & Lyndo

Please see the attached pdf, attaching logo as well.

Target Market(s)

Ride Sharing, Taxi

Industry/Entity Type

Business

Number of Pages Required

5+ page

Requirements
Must have
• Icons/graphics, How it works icons, case studies icons, all mentioned pages
Should not have
• Not much yellow color

```html
<!DOCTYPE html>
<html lang="en">
<head>
<meta charset="utf-8">
<title>Farovo — Low Bids, Lowest Fares</title>
<link href="https://fonts.googleapis.com/css2?family=Roboto:wght@400;500;700&family=Raleway:wght@400;500;600&display=swap" rel="stylesheet">
<style>
  :root{
    --red:#e31e24;
    --ink:#222222;
    --text:#555555;
    --muted:#8a8a8a;
    --line:#e9e9e9;
    --footer:#2f2f2f;
    --footer-text:#a9a9a9;
    --white:#ffffff;
  }
  *{box-sizing:border-box;margin:0;padding:0}
  html,body{width:1200px;height:2347px;overflow:hidden;background:var(--white)}
  body{position:relative;font-family:"Roboto",Arial,sans-serif;color:var(--ink)}
  a{color:inherit;text-decoration:none}

  .site-header{position:absolute;left:0;top:0;width:1200px;height:70px;border-bottom:1px solid var(--line);background:var(--white)}
  .menu-toggle{position:absolute;left:30px;top:31px;width:16px;height:9px;border-top:2px solid #444;border-bottom:2px solid #444}
  .menu-toggle::after{content:"";position:absolute;left:0;top:1.5px;width:16px;height:2px;background:#444}
  .brand{position:absolute;left:118px;top:22px;display:flex;align-items:center;gap:7px;font-weight:700;font-size:15px;letter-spacing:1px;color:var(--ink)}
  .brand-dot{width:12px;height:12px;border-radius:50%;background:var(--red)}
  .nav{position:absolute;top:27px;font-size:12px;color:#555}
  .nav a{position:absolute;white-space:nowrap}

  .tagline{position:absolute;left:0;top:98px;width:1200px;text-align:center;font-size:22px;font-weight:400;color:#444}
  .tagline strong{color:var(--red);font-weight:700}

  .hero{position:absolute;left:0;top:153px;width:1200px;height:465px;
    background:radial-gradient(ellipse at 62% 5%,#fff4c8 0%,#f4b24a 18%,rgba(200,120,40,.6) 40%,transparent 62%),
    linear-gradient(160deg,#7c6a2a 0%,#9a8640 30%,#5a4a3a 55%,#2d2a2c 100%)}
  .hero-dots{position:absolute;left:135px;top:580px;display:flex;gap:3px}
  .hero-dots span{width:7px;height:7px;border-radius:50%;background:rgba(255,255,255,.55)}
  .hero-dots span:first-child{background:#fff}

  .feature{position:absolute;width:301px;height:391px;border:1px solid var(--line);background:var(--white)}
  .feature-photo{height:180px}
  .feature h3{position:absolute;left:28px;top:206px;font-size:14.5px;font-weight:500;color:var(--ink)}
  .feature p{position:absolute;left:28px;top:240px;width:250px;font-family:"Raleway",Arial,sans-serif;font-size:11px;line-height:19.6px;color:var(--text)}
  .learn-more{position:absolute;left:28px;top:350px;font-size:9.5px;font-weight:700;color:var(--red);display:flex;align-items:center;gap:4px}
  .learn-more::after{content:"";border-left:4px solid var(--red);border-top:3.5px solid transparent;border-bottom:3.5px solid transparent}

  .skyline{position:absolute;left:410px;top:1862px;width:790px;height:200px;
    background:linear-gradient(90deg,#f08a4a 0%,#d94a7a 25%,#3fb9a6 45%,#e2506a 65%,#6a4c9c 80%,#2fb7b0 100%);opacity:.85}
  .footer-wave{position:absolute;left:0;top:1990px;width:1200px;height:80px}
  .site-footer{position:absolute;left:0;top:2068px;width:1200px;height:279px;background:var(--footer);color:var(--footer-text)}
  .footer-brand{position:absolute;left:135px;top:44px;width:126px;text-align:center}
  .footer-brand-dot{display:block;margin:0 auto 10px;width:38px;height:38px;border-radius:50%;border:3px solid #8f8f8f}
  .footer-brand-name{font-size:24px;font-weight:400;letter-spacing:2px;color:#9a9a9a}
  .footer-divider{position:absolute;left:323px;top:42px;width:1px;height:132px;background:#444}
  .footer-col{position:absolute;top:48px}
  .footer-col h4{font-size:14px;font-weight:500;color:#f2f2f2;margin-bottom:14px}
  .footer-col li{list-style:none;font-family:"Raleway",Arial,sans-serif;font-size:11px;line-height:19.4px}
  .social li{display:flex;align-items:center;gap:8px;line-height:28.5px}
  .social li::before{content:"";width:9px;height:9px;border-radius:50%;border:1.5px solid var(--footer-text)}
  .store-badge{display:block;width:171px;height:50px;border-radius:7px;background:#000;border:1px solid #777;margin-bottom:8px}
  .footer-bottom{position:absolute;left:0;top:221px;width:1200px;border-top:1px solid #3d3d3d}
  .footer-bottom span{position:absolute;top:23px;font-size:10.5px;white-space:nowrap}
</style>
</head>
<body>

<header class="site-header">
  <div class="menu-toggle"></div>
  <a class="brand" href="#"><span class="brand-dot"></span>FAROVO</a>
  <nav class="nav">
    <a href="#" style="left:274px">Ride</a>
    <a href="#" style="left:329px">Drive</a>
    <a href="#" style="left:1081px">Help</a>
    <a href="#" style="left:1136px">Sign In</a>
  </nav>
</header>

<h1 class="tagline"><strong>Roam Around</strong> Low Bids, Lowest Fares</h1>

<section class="hero" role="img" aria-label="Sunlit country road seen from a moving car with its side mirror"></section>
<div class="hero-dots"><span></span><span></span><span></span><span></span><span></span></div>

<article class="feature" style="left:135px;top:679px">
  <div class="feature-photo" role="img" aria-label="Man relaxing on a sofa with a laptop" style="background:linear-gradient(135deg,#8a8680,#d9d4cc 60%,#6b6660)"></div>
  <h3>Instant Bids, Slashed Fares</h3>
  <p>Lorem Ipsum is simply dummy text of the used printing and typesetting industry. Lorem asos Ipsum has been the industry's standard pints unknown printer took a galley of type and type make a type specimen book.</p>
  <a class="learn-more" href="#">LEARN MORE</a>
</article>
<article class="feature" style="left:449px;top:679px">
  <div class="feature-photo" role="img" aria-label="Hands holding a tablet with a clock and calendar" style="background:linear-gradient(135deg,#2a2a2c,#55524e 55%,#1c1c1e)"></div>
  <h3>Automated Bidding, Saves Time</h3>
  <p>Lorem Ipsum is simply dummy text of the used printing and typesetting industry. Lorem asos Ipsum has been the industry's standard pints unknown printer took a galley of type and type make a type specimen book.</p>
  <a class="learn-more" href="#">LEARN MORE</a>
</article>
<article class="feature" style="left:763px;top:679px">
  <div class="feature-photo" role="img" aria-label="Smiling driver at the wheel of a car" style="background:linear-gradient(135deg,#c9ccd0,#4a4f58 55%,#2a2d33)"></div>
  <h3>Speedy Service Antwhere, Anytime</h3>
  <p>Lorem Ipsum is simply dummy text of the used printing and typesetting industry. Lorem asos Ipsum has been the industry's standard pints unknown printer took a galley of type and type make a type specimen book.</p>
  <a class="learn-more" href="#">LEARN MORE</a>
</article>

<article class="feature" style="left:135px;top:1092px">
  <div class="feature-photo" role="img" aria-label="Business handshake in front of a car" style="background:linear-gradient(135deg,#b5332e,#c9b9aa 45%,#9fb6cf)"></div>
  <h3>Multiple Hiring, Huge Discounts</h3>
  <p>Lorem Ipsum is simply dummy text of the used printing and typesetting industry. Lorem asos Ipsum has been the industry's standard pints unknown printer took a galley of type and type make a type specimen book.</p>
  <a class="learn-more" href="#">LEARN MORE</a>
</article>
<article class="feature" style="left:449px;top:1092px">
  <div class="feature-photo" role="img" aria-label="Hands on a steering wheel at sunset" style="background:linear-gradient(180deg,#f2c46a,#b06a3a 45%,#4a2a22)"></div>
  <h3>Luxury Hires</h3>
  <p>Lorem Ipsum is simply dummy text of the used printing and typesetting industry. Lorem asos Ipsum has been the industry's standard pints unknown printer took a galley of type and type make a type specimen book.</p>
  <a class="learn-more" href="#">LEARN MORE</a>
</article>
<article class="feature" style="left:763px;top:1092px">
  <div class="feature-photo" role="img" aria-label="Woman dropping a coin into a pink piggy bank" style="background:linear-gradient(135deg,#efe4da,#e86aa0 45%,#d8c6b8)"></div>
  <h3>Save Smart</h3>
  <p>Lorem Ipsum is simply dummy text of the used printing and typesetting industry. Lorem asos Ipsum has been the industry's standard pints unknown printer took a galley of type and type make a type specimen book.</p>
  <a class="learn-more" href="#">LEARN MORE</a>
</article>

<article class="feature" style="left:135px;top:1507px">
  <div class="feature-photo" role="img" aria-label="Child buckled into a car seat" style="background:linear-gradient(135deg,#3a3330,#b59a78 50%,#5a5070)"></div>
  <h3>Safe Travel</h3>
  <p>Lorem Ipsum is simply dummy text of the used printing and typesetting industry. Lorem asos Ipsum has been the industry's standard pints unknown printer took a galley of type and type make a type specimen book.</p>
  <a class="learn-more" href="#">LEARN MORE</a>
</article>

<div class="skyline" role="img" aria-label="Colourful illustrated skyline of world city landmarks"></div>
<svg class="footer-wave" viewBox="0 0 1200 80" preserveAspectRatio="none" aria-hidden="true">
  <path d="M0 80 L0 52 C120 8 230 8 330 40 C430 72 520 28 640 20 C760 12 820 50 940 50 C1040 50 1110 10 1200 22 L1200 80 Z" fill="#2f2f2f"/>
</svg>

<footer class="site-footer">
  <div class="footer-brand">
    <span class="footer-brand-dot"></span>
    <span class="footer-brand-name">FAROVO</span>
  </div>
  <div class="footer-divider"></div>

  <div class="footer-col" style="left:369px">
    <h4>Quick Links</h4>
    <ul><li>Ride</li><li>Drive</li><li>Cities</li><li>Fare Estimate</li><li>How It Works</li><li>Help</li></ul>
  </div>
  <div class="footer-col" style="left:527px">
    <h4>Top Cities</h4>
    <ul><li>San Francisco</li><li>London</li><li>Los Angeles</li><li>Washington D.C.</li><li>Mexico City</li><li>São Paulo</li></ul>
  </div>
  <div class="footer-col social" style="left:685px">
    <h4 style="margin-bottom:6px">We're Social</h4>
    <ul><li>Friendloop</li><li>Chirper</li><li>WorkLink</li><li>Snapgram</li></ul>
  </div>
  <div class="footer-col" style="left:843px">
    <h4 style="margin-bottom:12px">Download</h4>
    <span class="store-badge"></span>
    <span class="store-badge"></span>
  </div>

  <div class="footer-bottom">
    <span style="left:135px">Copyright 2017 Farovo.</span>
    <span style="left:914px">Terms of Use</span>
    <span style="left:995px">Privacy Policy</span>
  </div>
</footer>

</body>
</html>
```